Winery Needs a flyer for a dinner show with a tribute band/show

We will have a dinner and show with hosted beer and wine. The show will be a tribute to the Moon Crew. The event will be on November 1, 2019 from 6pm-10pm with dinner starting at 6:30pm. Would like to have on the flyer GTL DinnerGuild Presents... A tribute to the Moon Crew. Enjoy an evening with the Stars under the Stars on the HillPaths.... Club Members $159.00 General Public $189.00 tickets can be purchased online at www.HillPathCellars.example, call in 555.304.7712 or at the Sipping Hall, 4870 Marbrook Court Larkmont, CO 90001. Included files as example and some of our logos. Just examples looking forward to your creativity.

Target Market(s)

Wine Drinkers, age 30-60, outdoor people

Font styles to use
Sans Serif
Other font styles liked:
• cottage and Barn

Colors

Designer to choose colors to be used in the design.

Requirements
Must have
• All important information to purchase tickets
Nice to have
• classic and reto if possible while still incorporating our logo somewhere

```html
<!DOCTYPE html>
<html lang="en">
<head>
<meta charset="utf-8">
<title>GTL DinnerGuild – A Tribute to the Moon Crew</title>
<link href="https://fonts.googleapis.com/css2?family=Cinzel:wght@400;500;600&family=Montserrat:wght@600;700&display=swap" rel="stylesheet">
<style>
  :root {
    --page: #ffffff;
    --night: #05060d;
    --indigo: #1a1f4a;
    --glow: #2f6cff;
    --ink: #f2f2f4;
    --rose: #e2646b;
    --rose-deep: #b3262e;
    --silver-hi: #ffffff;
    --silver-lo: #8d8f98;
    --sepia: #6d6458;
  }
  * { margin: 0; padding: 0; box-sizing: border-box; }
  html, body { width: 1200px; height: 830px; overflow: hidden; background: var(--page); }
  .flyer {
    position: absolute; left: 317px; top: 15px; width: 565px; height: 800px;
    background:
      radial-gradient(ellipse 70% 45% at 40% 38%, rgba(40,50,120,.45), transparent 70%),
      linear-gradient(180deg, var(--indigo) 0%, var(--night) 55%, #000 100%);
    color: var(--ink); font-family: "Cinzel", serif; text-align: center; overflow: hidden;
  }
  .flyer__photo {
    position: absolute; left: 196px; top: 0; width: 369px; height: 420px;
    background: radial-gradient(ellipse at 60% 30%, #b8ad9c 0%, var(--sepia) 45%, #1c1a22 90%);
    -webkit-mask-image: linear-gradient(90deg, transparent 0%, #000 30%), linear-gradient(180deg, #000 55%, transparent 100%);
    -webkit-mask-composite: source-in;
    mask-image: linear-gradient(90deg, transparent 0%, #000 30%), linear-gradient(180deg, #000 55%, transparent 100%);
    mask-composite: intersect;
  }
  .brand {
    position: absolute; left: 10px; top: 120px; width: 210px;
    display: flex; align-items: center; justify-content: center; gap: 8px;
    font-size: 15px; font-weight: 500; color: var(--ink); white-space: nowrap;
  }
  .brand__dot { width: 10px; height: 10px; border-radius: 50%; background: var(--rose-deep); flex: none; }
  .presents { position: absolute; left: 10px; top: 225px; width: 210px; font-family: "Montserrat", sans-serif; font-weight: 600; font-size: 9px; letter-spacing: 4px; }
  .kicker { position: absolute; left: 38px; top: 287px; font-size: 18px; letter-spacing: 11px; text-align: left; white-space: nowrap; }
  .headline {
    position: absolute; left: 30px; top: 312px; width: 520px; text-align: left; white-space: nowrap;
    font-size: 70px; font-weight: 500; letter-spacing: -1px; line-height: 1;
    background: linear-gradient(180deg, var(--silver-hi) 10%, var(--silver-lo) 55%, var(--silver-hi) 90%);
    -webkit-background-clip: text; background-clip: text; color: transparent;
  }
  .tagline { position: absolute; left: 0; right: 0; top: 438px; font-size: 18px; line-height: 1.45; }
  .divider {
    position: absolute; left: 120px; width: 325px; height: 2px;
    background: radial-gradient(ellipse at center, var(--glow) 0%, rgba(47,108,255,.35) 35%, transparent 75%);
  }
  .date { position: absolute; left: 0; right: 0; top: 537px; font-size: 34px; color: var(--rose); }
  .time { position: absolute; left: 0; right: 0; top: 587px; font-size: 13px; }
  .prices { position: absolute; left: 0; right: 0; top: 652px; font-size: 17px; line-height: 1.6; }
  .prices strong { color: var(--rose); font-weight: 600; }
  .tickets { position: absolute; left: 0; right: 0; top: 747px; font-size: 13px; }
  .button {
    position: absolute; left: 131px; top: 772px; width: 303px; height: 41px; border-radius: 21px;
    background: linear-gradient(180deg, #e97b80 0%, var(--rose-deep) 60%, #8e1a22 100%);
    border: 2px solid #f3c5c7; display: flex; align-items: center; justify-content: center;
    font-size: 15px; font-weight: 600; letter-spacing: .5px; color: #fff;
  }
  .footer {
    position: absolute; left: 0; right: 0; top: 840px;
    font-family: "Montserrat", sans-serif; font-weight: 700; font-size: 11.3px; white-space: nowrap;
  }
  .footer span { color: var(--rose); font-weight: 600; }
  .flyer { height: 900px; transform: scale(0.8889); transform-origin: top left; width: 635.6px; }
</style>
</head>
<body>
  <main class="flyer">
    <div class="flyer__photo" role="img" aria-label="Sepia photograph of three laughing entertainers in tuxedos" style="left:220px;width:416px;height:472px"></div>
    <div class="brand"><span class="brand__dot"></span>GTL DinnerGuild</div>
    <p class="presents">PRESENTS</p>
    <p class="kicker">A TRIBUTE TO THE</p>
    <h1 class="headline" style="font-size:78px">MOON CREW</h1>
    <p class="tagline" style="font-size:20px">ENJOY AN EVENING WITH THE STARS<br>UNDER THE STARS ON THE HILLPATHS....</p>
    <div class="divider" style="top:517px;left:135px;width:366px"></div>
    <p class="date" style="font-size:38px">NOVEMBER 1, 2019</p>
    <p class="time" style="font-size:14.5px">FROM 6PM-10PM WITH DINNER STARTING AT 6:30PM.</p>
    <div class="divider" style="top:640px;left:135px;width:366px"></div>
    <p class="prices" style="font-size:19px">CLUB MEMBERS : <strong>$159.00</strong><br>GENERAL PUBLIC : <strong>$189.00</strong></p>
    <div class="divider" style="top:723px;left:135px;width:366px"></div>
    <p class="tickets" style="font-size:14.5px">TICKETS CAN BE PURCHASED ONLINE AT</p>
    <div class="button" style="left:147px;width:341px;height:46px;border-radius:23px;font-size:17px">WWW.HILLPATHCELLARS.EXAMPLE</div>
    <p class="footer" style="font-size:12.5px">555.304.7712 <span>OR AT THE SIPPING HALL,</span> 4870 MARBROOK COURT LARKMONT, CO 90001</p>
  </main>
</body>
</html>
```